Quorvane Learning App for Children with Dyslexia

Project Description:

We are seeking a talented UI/UX designer to create engaging and intuitive designs for Quorvane, an innovative educational app designed to help children learn letters and words through a multisensory learning approach. The app aims to be particularly helpful for children with dyslexia, providing a supportive and interactive learning environment.

Key App Features & Design Requirements:

Account Creation Screen: Design a welcoming and straightforward sign-up page that allows users to register with their email or continue with Brindlewave. The design should be clean, focusing on user-friendliness and accessibility, adhering to our terms of service and privacy policy.

Main Screen Design: The main screen should allocate at least 4/6 of its height to the interactive drawing area. It needs to display word prompts in both correct and scrambled orders and include options to "Show all Words," "Play all words," and a search function. The interface should be vibrant, engaging, and easy to navigate for children.

Profile Section: Create a user-friendly profile page that allows users to edit their profile image, name, username, email, links, and bio. The design should be clean and encourage user engagement.

QuorTally Page: This section will display the user's learning progress, including rankings, a learning curve, and recently learned words. It should visually represent progress in a motivating and understandable way, suitable for a younger audience.

Visual and Auditory Feedback Implementation: Incorporate elements that support visual and auditory feedback, using dyslexia-friendly formats. This includes choosing appropriate colors, fonts, and auditory cues.

Accessibility and Customization Settings: Designs should include settings for adjusting visual contrast, font size, and the word list to accommodate individual preferences and needs.

Feel free to add more interactions and/or pages.

Design preferences:

Color Scheme: Use a bright, inviting color palette that stimulates learning and engagement without overwhelming the users.
Font Selection: Opt for fonts that are readable and accessible, particularly for users with dyslexia.
Icons and Graphics: Design custom icons and graphics that are cohesive with the app's theme and purpose. Illustrations should be simple, relatable, and supportive of the learning process.

Target Market(s)

Educational

Industry/Entity Type

Educational

Colors
0054AA
0677BA
7BADD7
CADEEF
E8F1F8
0094D4
00A9DD
6FCCEA
C7EBF8
E9F6FB

Requirements
Must have
• Educational app, a writing area, scoring and account management
Nice to have
• Statistics, Ranking Page, Settings and some nice visual features

```html
<!DOCTYPE html>
<html lang="en">
<head>
<meta charset="utf-8">
<title>Quorvane – App Screens</title>
<link rel="stylesheet" href="https://fonts.googleapis.com/css2?family=Poppins:wght@400;500;600;700&display=swap">
<style>
  :root{
    --board:#96b9ec;
    --navy:#0054aa;
    --brand:#0677ba;
    --sky:#0094d4;
    --cyan:#00a9dd;
    --aqua:#6fccea;
    --ice:#c7ebf8;
    --mist:#e9f6fb;
    --line:#cadeef;
    --ink:#1d1d1f;
    --muted:#6b7280;
    --gold:#f7c21c;
    --violet-a:#9a48d0;
    --violet-b:#d7a2f7;
    --dim:#9ba3ab;
  }
  *{box-sizing:border-box;margin:0;padding:0}
  html,body{width:920px;height:1200px;overflow:hidden;background:var(--board)}
  body{font-family:"Poppins",sans-serif;color:var(--ink)}
  .board{position:relative;width:920px;height:1200px;background:var(--board)}
  .phone{position:absolute;width:236px;height:521px;border-radius:24px;overflow:hidden;
    background:linear-gradient(180deg,#ffffff 0%,var(--ice) 45%,#ffffff 100%);
    box-shadow:0 14px 30px rgba(40,80,150,.28)}
  .phone--splash{left:63px;top:58px}
  .phone--signup{left:342px;top:58px;background:linear-gradient(180deg,#fff 0%,var(--ice) 50%,#fff 100%)}
  .phone--home{left:620px;top:58px;background:linear-gradient(180deg,#fff 0%,var(--mist) 60%,var(--ice) 85%,#fff 100%)}
  .phone--stats{left:63px;top:621px;background:linear-gradient(180deg,#fff 0%,var(--mist) 50%,#fff 100%)}
  .phone--profile{left:342px;top:621px;background:linear-gradient(180deg,#fff 0%,var(--ice) 40%,var(--mist) 75%,#fff 100%)}
  .phone--menu{left:620px;top:621px;background:var(--dim)}
  .abs{position:absolute;line-height:1;white-space:nowrap}
  .status-time{left:19px;top:8px;font-size:10px;font-weight:600}
  .status-icons{position:absolute;left:172px;top:9px}
  .home-bar{position:absolute;left:81px;bottom:10px;width:76px;height:2.5px;border-radius:2px;background:#777}
  .center{left:0;width:100%;text-align:center}
  .wordmark{font-weight:700;color:var(--brand);letter-spacing:-.5px}
  .tagline{color:var(--sky);font-weight:400}
  .art{position:absolute;border-radius:10px}
  .field-label{font-size:8px;color:#555;font-weight:500}
  .field{position:absolute;background:#fff;border:1px solid #e3edf5;border-radius:6px}
  .btn{position:absolute;display:flex;align-items:center;justify-content:center;font-weight:600;border-radius:18px}
  .btn--primary{background:var(--brand);color:#fff}
  .social{position:absolute;width:25px;height:25px;border-radius:50%;background:#fff;box-shadow:0 1px 4px rgba(0,0,0,.12)}
  .avatar{position:absolute;border-radius:50%;background:radial-gradient(circle at 50% 40%,#a37a5c,#4a3326)}
  .panel{position:absolute;background:#fff;border:1px solid var(--line);border-radius:6px}
  .chip{position:absolute;width:60px;height:20px;border:1px solid var(--aqua);border-radius:3px;background:#fff;
    font-size:5px;font-weight:500;display:flex;align-items:center;justify-content:center}
  .chip--ghost{color:#aaa;border-color:var(--line)}
  .rank-card{position:absolute;width:101px;height:42px;border-radius:4px;color:#fff;padding:0 9px}
  .rank-card--total{left:12px;top:100px;background:linear-gradient(135deg,var(--sky),var(--brand))}
  .rank-card--daily{left:122px;top:100px;background:linear-gradient(135deg,var(--violet-a),var(--violet-b))}
  .rank-card .label{position:absolute;top:10px;font-size:5.5px}
  .rank-card .value{position:absolute;top:20px;font-size:11px;font-weight:600}
  .rank-card sup{font-size:6px}
  .axis{font-size:6.5px;color:#222;line-height:1.2}
  .tab{font-size:9.5px;font-weight:500}
  .drawer{position:absolute;left:0;top:0;width:188px;height:521px;background:linear-gradient(180deg,var(--cyan),var(--brand));color:#fff;z-index:2}
  .drawer-item{position:absolute;left:16px;display:flex;align-items:center;gap:10px;font-size:9.5px;font-weight:600}
</style>
</head>
<body>
<div class="board">

  <!-- Splash -->
  <section class="phone phone--splash">
    <div class="abs status-time">9:41</div>
    <svg class="status-icons" width="46" height="9" viewBox="0 0 46 9"><rect x="0" y="6" width="2" height="3" fill="#222"/><rect x="3" y="4" width="2" height="5" fill="#222"/><rect x="6" y="2" width="2" height="7" fill="#222"/><rect x="9" y="0" width="2" height="9" fill="#bbb"/><path d="M16 3.5a6 6 0 0 1 8 0M17.5 5.3a3.6 3.6 0 0 1 5 0" stroke="#222" stroke-width="1.3" fill="none"/><circle cx="20" cy="7.5" r="1" fill="#222"/><rect x="29" y="1" width="15" height="7" rx="2" fill="#222"/><rect x="44.5" y="3" width="1.2" height="3" fill="#222"/></svg>
    <div class="art" role="img" aria-label="Illustration of a girl with a graduation cap standing on a stack of books" style="left:41px;top:182px;width:180px;height:148px;background:linear-gradient(160deg,rgba(111,204,234,.35),rgba(233,246,251,.6))"></div>
    <div style="position:absolute;left:24px;top:331px;width:196px;height:1px;background:#c8d4dc"></div>
    <div class="abs center wordmark" style="top:356px;font-size:35px">Quorvane</div>
    <div class="abs center tagline" style="top:391px;font-size:10px">Learn letters and words</div>
    <div class="home-bar"></div>
  </section>

  <!-- Sign up -->
  <section class="phone phone--signup">
    <div class="abs status-time">9:41</div>
    <svg class="status-icons" width="46" height="9" viewBox="0 0 46 9"><rect x="0" y="6" width="2" height="3" fill="#222"/><rect x="3" y="4" width="2" height="5" fill="#222"/><rect x="6" y="2" width="2" height="7" fill="#222"/><rect x="9" y="0" width="2" height="9" fill="#bbb"/><path d="M16 3.5a6 6 0 0 1 8 0M17.5 5.3a3.6 3.6 0 0 1 5 0" stroke="#222" stroke-width="1.3" fill="none"/><circle cx="20" cy="7.5" r="1" fill="#222"/><rect x="29" y="1" width="15" height="7" rx="2" fill="#222"/><rect x="44.5" y="3" width="1.2" height="3" fill="#222"/></svg>
    <div class="abs center wordmark" style="top:62px;font-size:22px">Quorvane</div>
    <div class="abs center tagline" style="top:84px;font-size:6px">Learn letters and words</div>
    <div class="abs wordmark" style="left:26px;top:156px;font-size:23px">Welcome,</div>
    <div class="abs" style="left:26px;top:184px;font-size:12px;color:#333">login to start with Quorvane 👋</div>
    <div class="abs field-label" style="left:26px;top:212px">Email</div>
    <div class="field" style="left:26px;top:238px;width:185px;height:28px"></div>
    <div class="abs" style="left:36px;top:248px;font-size:9.5px;color:#333">milo.renshaw@postvale.com</div>
    <div class="btn btn--primary" style="left:24px;top:279px;width:185px;height:28px;font-size:9.5px">Sign up with email</div>
    <div style="position:absolute;left:52px;top:331px;width:34px;height:1px;background:#cfd8df"></div>
    <div class="abs center" style="top:327px;font-size:8px;color:#555">or sign in with</div>
    <div style="position:absolute;left:151px;top:331px;width:34px;height:1px;background:#cfd8df"></div>
    <div class="social" style="left:76px;top:346px" aria-label="Sign in with Brindlewave"></div>
    <div class="social" style="left:106px;top:346px" aria-label="Sign in with social account"></div>
    <div class="social" style="left:136px;top:346px" aria-label="Sign in with device account"></div>
    <div class="abs center" style="top:382px;font-size:8px;color:#555">By clicking continue, you agree to our</div>
    <div class="abs center" style="top:395px;font-size:8px;color:#555"><b style="font-weight:500;color:#222">Terms of Service</b> and <b style="font-weight:500;color:#222">Privacy Policy</b></div>
    <div class="home-bar"></div>
  </section>

  <!-- Home / drawing -->
  <section class="phone phone--home">
    <div class="abs status-time">9:41</div>
    <svg class="status-icons" width="46" height="9" viewBox="0 0 46 9"><rect x="0" y="6" width="2" height="3" fill="#222"/><rect x="3" y="4" width="2" height="5" fill="#222"/><rect x="6" y="2" width="2" height="7" fill="#222"/><rect x="9" y="0" width="2" height="9" fill="#bbb"/><path d="M16 3.5a6 6 0 0 1 8 0M17.5 5.3a3.6 3.6 0 0 1 5 0" stroke="#222" stroke-width="1.3" fill="none"/><circle cx="20" cy="7.5" r="1" fill="#222"/><rect x="29" y="1" width="15" height="7" rx="2" fill="#222"/><rect x="44.5" y="3" width="1.2" height="3" fill="#222"/></svg>
    <div class="avatar" role="img" aria-label="Profile photo of the child user" style="left:11px;top:33px;width:28px;height:28px"></div>
    <div class="abs" style="left:45px;top:42px;font-size:10px;font-weight:600">Hi, Corin 👋</div>
    <div style="position:absolute;left:123px;top:39px;width:52px;height:17px;border-radius:9px;background:var(--gold);display:flex;align-items:center;padding-left:2px;gap:3px">
      <span style="width:13px;height:13px;border-radius:50%;background:#fbd866;display:flex;align-items:center;justify-content:center;color:#fff;font-size:8px">★</span>
      <span style="font-size:5.5px;color:#fff;font-weight:600">150 Points</span>
    </div>
    <svg style="position:absolute;left:186px;top:41px" width="13" height="13" viewBox="0 0 13 13"><circle cx="6.5" cy="6.5" r="4.3" fill="none" stroke="var(--sky)" stroke-width="1.3" stroke-dasharray="2 1.2"/><circle cx="6.5" cy="6.5" r="1.8" fill="none" stroke="var(--sky)" stroke-width="1.1"/></svg>
    <svg style="position:absolute;left:210px;top:41px" width="12" height="11" viewBox="0 0 12 11"><path d="M0 1.5h12M0 5.5h12M0 9.5h12" stroke="var(--brand)" stroke-width="1.5"/></svg>
    <div class="panel" aria-label="Drawing area" style="left:12px;top:72px;width:211px;height:223px"></div>
    <div class="btn" style="left:13px;top:306px;width:101px;height:34px;border-radius:3px;background:var(--cyan);color:#fff;font-size:9px">Show all Words</div>
    <div class="btn" style="left:122px;top:306px;width:101px;height:34px;border-radius:3px;background:#fff;border:1px solid var(--aqua);font-size:9px">Play all Words</div>
    <div class="panel" style="left:12px;top:348px;width:211px;height:113px">
      <div class="chip" style="left:10px;top:10px">Lorem</div><div class="chip" style="left:75px;top:10px">Lorem</div><div class="chip" style="left:139px;top:10px">Lorem</div>
      <div class="chip" style="left:10px;top:34px">Lorem</div><div class="chip" style="left:75px;top:34px">Lorem</div><div class="chip" style="left:139px;top:34px">Lorem</div>
      <div class="chip" style="left:10px;top:59px">Lorem</div><div class="chip" style="left:75px;top:59px">Lorem</div><div class="chip" style="left:139px;top:59px">Lorem</div>
      <div class="chip" style="left:10px;top:83px">Lorem</div><div class="chip" style="left:75px;top:83px">Lorem</div><div class="chip" style="left:139px;top:83px">Lorem</div>
    </div>
    <div class="btn btn--primary" style="left:56px;top:468px;width:125px;height:28px;font-size:9px">Show me the results</div>
    <div class="home-bar"></div>
  </section>

  <!-- Stats -->
  <section class="phone phone--stats">
    <div class="abs status-time">9:41</div>
    <svg class="status-icons" width="46" height="9" viewBox="0 0 46 9"><rect x="0" y="6" width="2" height="3" fill="#222"/><rect x="3" y="4" width="2" height="5" fill="#222"/><rect x="6" y="2" width="2" height="7" fill="#222"/><rect x="9" y="0" width="2" height="9" fill="#bbb"/><path d="M16 3.5a6 6 0 0 1 8 0M17.5 5.3a3.6 3.6 0 0 1 5 0" stroke="#222" stroke-width="1.3" fill="none"/><circle cx="20" cy="7.5" r="1" fill="#222"/><rect x="29" y="1" width="15" height="7" rx="2" fill="#222"/><rect x="44.5" y="3" width="1.2" height="3" fill="#222"/></svg>
    <div class="avatar" role="img" aria-label="Profile photo of the child user" style="left:19px;top:32px;width:28px;height:28px"></div>
    <div class="abs center" style="top:41px;font-size:9.5px;font-weight:500">QuorTally</div>
    <svg style="position:absolute;left:186px;top:41px" width="13" height="13" viewBox="0 0 13 13"><circle cx="6.5" cy="6.5" r="4.3" fill="none" stroke="var(--sky)" stroke-width="1.3" stroke-dasharray="2 1.2"/><circle cx="6.5" cy="6.5" r="1.8" fill="none" stroke="var(--sky)" stroke-width="1.1"/></svg>
    <svg style="position:absolute;left:210px;top:42px" width="12" height="11" viewBox="0 0 12 11"><path d="M0 1.5h12M0 5.5h12M0 9.5h12" stroke="var(--brand)" stroke-width="1.5"/></svg>
    <div class="abs tab" style="left:15px;top:75px">Ranking</div>
    <div style="position:absolute;left:15px;top:88px;width:39px;height:1.5px;background:var(--aqua)"></div>
    <div class="abs tab" style="left:89px;top:75px">Correct words</div>
    <div class="abs tab" style="left:190px;top:75px">Today</div>
    <div class="rank-card rank-card--total"><span class="abs label">Total Ranking</span><span class="abs value">1<sup>st</sup> Place of 100</span></div>
    <div class="rank-card rank-card--daily"><span class="abs label">Daily Ranking</span><span class="abs value">10<sup>th</sup> Place of 100</span></div>
    <div class="panel" style="left:11px;top:151px;width:211px;height:216px;border-radius:4px"></div>
    <div style="position:absolute;left:44px;top:160px;width:173px;height:176px;background:#f7f8fa"></div>
    <div class="abs axis" style="left:19px;top:161px">2000<br>words</div>
    <div class="abs axis" style="left:19px;top:203px">1500<br>words</div>
    <div class="abs axis" style="left:19px;top:246px">1000<br>words</div>
    <div class="abs axis" style="left:19px;top:284px">500<br>words</div>
    <div class="abs axis" style="left:21px;top:330px">0</div>
    <svg style="position:absolute;left:0;top:0" width="236" height="521" viewBox="0 0 236 521"><polyline points="44.9,334.6 73.4,328 93.6,302.3 102.9,306.7 127,269.4 134.7,271.6 144.6,244.2 157.7,264.5 169.8,227.8 187.3,238.8 193.9,202.1" fill="none" stroke="var(--cyan)" stroke-width="1.4"/><circle cx="193.9" cy="202.1" r="4.5" fill="var(--cyan)"/></svg>
    <div class="abs axis" style="left:43px;top:348px">Sun</div>
    <div class="abs axis" style="left:69px;top:348px">Mon</div>
    <div class="abs axis" style="left:96px;top:348px">Tue</div>
    <div class="abs axis" style="left:121px;top:348px">Wed</div>
    <div class="abs axis" style="left:148px;top:348px">Thur</div>
    <div class="abs axis" style="left:176px;top:348px">Fri</div>
    <div class="abs axis" style="left:197px;top:348px">Sat</div>
    <div class="panel" style="left:11px;top:377px;width:211px;height:111px;border-radius:4px">
      <div class="abs" style="left:10px;top:9px;font-size:9px;font-weight:500">Recently Learned words</div>
      <div class="chip" style="left:10px;top:25px">Lorem</div><div class="chip" style="left:74px;top:25px">Lorem</div><div class="chip" style="left:138px;top:25px">Lorem</div>
      <div class="chip" style="left:10px;top:49px">Lorem</div><div class="chip" style="left:74px;top:49px">Lorem</div><div class="chip" style="left:138px;top:49px">Lorem</div>
      <div class="chip" style="left:10px;top:73px">Lorem</div><div class="chip chip--ghost" style="left:74px;top:73px">+ Add word</div>
    </div>
    <div class="home-bar"></div>
  </section>

  <!-- Profile -->
  <section class="phone phone--profile">
    <div class="abs status-time">9:41</div>
    <svg class="status-icons" width="46" height="9" viewBox="0 0 46 9"><rect x="0" y="6" width="2" height="3" fill="#222"/><rect x="3" y="4" width="2" height="5" fill="#222"/><rect x="6" y="2" width="2" height="7" fill="#222"/><rect x="9" y="0" width="2" height="9" fill="#bbb"/><path d="M16 3.5a6 6 0 0 1 8 0M17.5 5.3a3.6 3.6 0 0 1 5 0" stroke="#222" stroke-width="1.3" fill="none"/><circle cx="20" cy="7.5" r="1" fill="#222"/><rect x="29" y="1" width="15" height="7" rx="2" fill="#222"/><rect x="44.5" y="3" width="1.2" height="3" fill="#222"/></svg>
    <svg style="position:absolute;left:20px;top:42px" width="12" height="9" viewBox="0 0 12 9"><path d="M11 4.5H1.5M5 1L1.5 4.5 5 8" stroke="#222" stroke-width="1.2" fill="none"/></svg>
    <div class="abs center" style="top:41px;font-size:9.5px;font-weight:500">Profile</div>
    <div class="avatar" role="img" aria-label="Profile photo of a child using a tablet" style="left:74px;top:64px;width:88px;height:88px"></div>
    <div class="abs center" style="top:158px;font-size:8.5px;color:var(--sky)">Edit profile image</div>
    <div class="abs field-label" style="left:25px;top:180px">Name</div>
    <div class="field" style="left:25px;top:192px;width:185px;height:28px;border:none"></div>
    <div class="abs field-label" style="left:25px;top:230px">Username</div>
    <div class="field" style="left:25px;top:243px;width:185px;height:28px;border:none"></div>
    <div class="abs field-label" style="left:25px;top:280px">Email</div>
    <div class="field" style="left:25px;top:292px;width:185px;height:28px;border:none"></div>
    <div class="abs field-label" style="left:25px;top:328px">Links</div>
    <div class="field" style="left:25px;top:341px;width:185px;height:28px;border:none"></div>
    <div class="abs" style="left:38px;top:351px;font-size:8px;color:#555">+ Add Link</div>
    <div class="abs field-label" style="left:25px;top:378px">Description</div>
    <div class="field" style="left:25px;top:391px;width:185px;height:49px;border:none"></div>
    <div class="btn btn--primary" style="left:137px;top:464px;width:77px;height:28px;font-size:9.5px">Save</div>
    <div class="home-bar"></div>
  </section>

  <!-- Settings drawer -->
  <section class="phone phone--menu">
    <svg style="position:absolute;left:188px;top:9px" width="30" height="9" viewBox="16 0 30 9"><path d="M16 3.5a6 6 0 0 1 8 0M17.5 5.3a3.6 3.6 0 0 1 5 0" stroke="#222" stroke-width="1.3" fill="none"/><circle cx="20" cy="7.5" r="1" fill="#222"/><rect x="29" y="1" width="15" height="7" rx="2" fill="#222"/></svg>
    <svg style="position:absolute;left:186px;top:41px" width="13" height="13" viewBox="0 0 13 13"><circle cx="6.5" cy="6.5" r="4.3" fill="none" stroke="#4a6d86" stroke-width="1.3" stroke-dasharray="2 1.2"/><circle cx="6.5" cy="6.5" r="1.8" fill="none" stroke="#4a6d86" stroke-width="1.1"/></svg>
    <svg style="position:absolute;left:210px;top:42px" width="12" height="11" viewBox="0 0 12 11"><path d="M0 1.5h12M0 5.5h12M0 9.5h12" stroke="#3b5d78" stroke-width="1.5"/></svg>
    <div style="position:absolute;left:170px;top:72px;width:53px;height:223px;border:1px solid #aeb8c0;border-radius:6px"></div>
    <div style="position:absolute;left:170px;top:306px;width:53px;height:34px;border:1px solid #5f8aa8;border-radius:3px"></div>
    <div style="position:absolute;left:170px;top:348px;width:53px;height:113px;border:1px solid #aeb8c0;border-radius:6px"></div>
    <div class="drawer">
      <div class="abs" style="left:16px;top:23px;font-size:22px;font-weight:700">Quorvane</div>
      <div class="abs" style="left:16px;top:46px;font-size:6px">Learn letters and words</div>
      <svg style="position:absolute;left:169px;top:25px" width="10" height="10" viewBox="0 0 10 10"><path d="M1 1l8 8M9 1L1 9" stroke="#fff" stroke-width="1.6"/></svg>
      <div class="drawer-item" style="top:88px"><svg width="14" height="14" viewBox="0 0 14 14"><circle cx="7" cy="7" r="6" fill="none" stroke="#fff" stroke-width="1.4"/><path d="M7 1a6 6 0 0 1 0 12z" fill="#fff"/></svg>Adjusting Contrast</div>
      <div class="drawer-item" style="top:121px"><svg width="14" height="14" viewBox="0 0 14 14"><path d="M1 2h12M7 2v11M4 7h6" stroke="#fff" stroke-width="1.5" fill="none"/></svg>Font Size</div>
      <div class="drawer-item" style="top:155px"><svg width="14" height="14" viewBox="0 0 14 14"><rect x="2" y="1.5" width="10" height="12" rx="1" fill="none" stroke="#fff" stroke-width="1.3"/><path d="M4.5 5h5M4.5 7.5h5M4.5 10h5" stroke="#fff" stroke-width="1.1"/></svg>Words List</div>
    </div>
  </section>

</div>
</body>
</html>
```